Women's Jewellery startup needs a captivating, beautifully designed and intuitive online store

[12/24 update]

Added 2 additional documents:

Feedback on designs received so far: designer feedback.docx
Product images from catalogue: products images.docx

Please read the feedback provided on designs provided so far to guide you further on your submission. The product images can be used to create promotional banners for the site.

@@@Added a document (VELISSE JEWELLERY_checklist.docx) which can be used by designers as a checklist when submitting their designs to ensure all aspects of the requirements have been covered @@@

+++IMPORTANT BUT NOT SPECIFIED IN THE REQUIREMENTS DOCUMENT - DESIGN SHOULD INCLUDE SUPPORT FOR MOBILE FRIENDLY SITE TOO+++

***Previous experience designing Jewellery online stores preferred (not essential)***

The name of the online Jewellery store is "Velisse Jewellery" and the business is based in Hong Kong. It will be run by 2 stay at home mothers. We need a Shopify themed store designed that will achieve the following objectives in order of priority:

• Conversion: The primary objective of the design/content is to prompt the customer to make a purchase. While this may sound obvious, it is mentioned so as not to distract the design process by focusing on other objectives (which are also important). The site also needs to be optimized so as to rank high in search engine searches for relevant keywords (SEO)
• Navigation: An intuitive interface which takes away a lot of the thinking from the customer by making it obvious what they need to do when they visit the store
• Engagement: Encourages the customer to spend time on the website and share content with their social network

Where applicable, the design of the store should reflect as closely as possible the mission statements and words outlined below:

• Jewellery you’ll fall in love with
• We want every client to leave the store with a smile
• We want to be able to provide the best service we can in every situation no matter what
• We aim to increase our business by word of mouth; therefore we tell people things about our store that makes it interesting for them to share
• We love every customer, no matter how difficult things get
• We, as a team, are so well informed about our products and brands that we always have the best information for our customers
• We celebrate women here!
• We celebrate life in here!
• We celebrate beauty here!
• We celebrate families here, as jewellery often stays within families.
• We will always try to make an extra step
• We will always try to exceed the expectation of our customers
• We will go as far as we possibly can to attract a customer back to our store and connect with us
• Every client that leaves our store knows more about jewellery because we passionately told him about it
• Romantic, classic, love, warm, cool, stylish

A draft functional specification is attached with this brief. We would like the design to reflect as closely as possible the functional requirements outlined in the document. Open to suggestions to improve upon the functional requirements.

Target Market(s)

Women aged 18-55

Industry/Entity Type

Jewelry Store

Coding

Coded - Design and coding required

Number of Pages Required

5+ page

Font styles to use
Other font styles liked:
• Myriad Pro as per Logo but open to any font that complements this one

Requirements
Must have
• 1. A look that encourages the user to make a purchase
• 2. An intuitive, easy to navigate and engaging interface
• 3. Primary colour scheme as defined in the functional specification attached
• 4. Simplistic look, not too cluttered
Nice to have
• 1. Closely matching the functional requirements of the site as outlined in the requirements specification but open to any better ideas

```html
<!DOCTYPE html>
<html lang="en">
<head>
<meta charset="utf-8">
<title>Velisse Jewellery – Online Store</title>
<link href="https://fonts.googleapis.com/css2?family=Open+Sans:wght@400;600;700&display=swap" rel="stylesheet">
<style>
:root{
  --gold:#c9a24a;
  --gold-dark:#a8852f;
  --ink:#222222;
  --text:#555555;
  --muted:#999999;
  --line:#e4e4e4;
  --card:#f2f2f2;
  --dark:#1b1b1b;
  --footer:#2b2b2b;
  --footer-bottom:#222222;
  --white:#ffffff;
}
*{box-sizing:border-box;margin:0;padding:0}
html,body{width:1200px;height:2348px;overflow:hidden}
body{font-family:"Open Sans",Arial,sans-serif;color:var(--text);background:var(--white);position:relative}
.wrap{width:944px;margin:0 auto;position:relative}

/* header */
.site-header{height:128px;background:var(--white)}
.utility-bar{position:absolute;right:0;top:8px;display:flex;gap:18px;font-size:10px;font-weight:600;letter-spacing:.5px;color:var(--muted);align-items:center}
.utility-bar .bag{background:var(--gold);color:var(--white);padding:3px 10px}
.brand{position:absolute;left:0;top:24px;display:flex;align-items:center;gap:12px}
.brand-mark{width:40px;height:40px;background:var(--gold)}
.brand-name{font-size:22px;font-weight:700;letter-spacing:3px;color:var(--gold);line-height:1}
.brand-tag{font-size:9px;color:var(--muted);margin-top:4px;letter-spacing:.5px}
.main-nav{position:absolute;right:0;top:70px;display:flex;gap:4px}
.main-nav a{font-size:11px;font-weight:600;color:var(--ink);text-decoration:none;padding:7px 14px;letter-spacing:.5px}
.main-nav a.active{background:var(--gold);color:var(--white)}

/* hero */
.hero{height:532px;position:relative;background:linear-gradient(90deg,#0d1014 0%,#161a20 40%,#3a3330 70%,#5a4a42 85%,#2a2624 100%)}
.hero-copy{position:absolute;left:128px;top:255px;font-size:44px;line-height:1.15;color:var(--white);font-weight:400}
.hero-copy strong{display:block;color:var(--gold);font-weight:700}
.hero-dots{position:absolute;left:128px;top:500px;display:flex;gap:10px}
.hero-dots span{width:9px;height:9px;border-radius:50%;background:#777}
.hero-dots span.on{background:var(--white)}

/* offers */
.offers{display:flex;gap:16px;margin-top:32px}
.offer{width:304px;height:228px;background:linear-gradient(180deg,#2a2a2a 0%,#121212 100%);color:var(--white);text-align:center;position:relative}
.offer-title{background:rgba(0,0,0,.55);font-size:20px;font-weight:700;letter-spacing:2px;padding:12px 0 8px;color:var(--gold)}
.offer-line{font-size:20px;margin-top:20px}
.offer-line b{color:var(--gold)}
.offer-sub{font-size:13px;margin-top:4px;letter-spacing:.5px}
.offer-amount{font-size:34px;font-weight:700;color:var(--gold);margin-top:2px}
.offer-date{font-size:10px;color:#bbb;margin-top:4px}

/* shop */
.shop{display:flex;gap:20px;margin-top:40px}
.filters{width:152px;flex-shrink:0}
.filters h2{font-size:14px;font-weight:700;color:var(--ink);letter-spacing:.5px;padding-bottom:10px;border-bottom:2px solid var(--ink)}
.filter-group{margin-top:18px}
.filter-group h3{font-size:11px;font-weight:700;color:var(--ink);letter-spacing:.5px;margin-bottom:8px}
.filter-group ul{list-style:none}
.filter-group li{font-size:11px;line-height:20px;display:flex;align-items:center;gap:7px;color:var(--text)}
.filter-group li::before{content:"";width:9px;height:9px;border:1px solid #bbb}
.price-range{margin-top:14px;position:relative;height:26px}
.price-range .track{position:absolute;left:0;right:0;top:10px;height:3px;background:var(--gold)}
.price-range .knob{position:absolute;top:5px;width:12px;height:12px;border-radius:50%;background:var(--white);border:2px solid var(--gold)}
.price-values{display:flex;justify-content:space-between;font-size:10px;color:var(--muted)}

.products{flex:1}
.products-head{display:flex;justify-content:space-between;align-items:center;padding-bottom:10px;border-bottom:1px solid var(--line)}
.products-head h2{font-size:14px;font-weight:700;color:var(--ink);letter-spacing:.5px}
.sorters{display:flex;gap:12px}
.sorters span{font-size:10px;color:var(--muted);border:1px solid var(--line);padding:3px 8px}
.grid{display:grid;grid-template-columns:repeat(3,246px);gap:24px 16px;margin-top:20px}
.card{height:270px;text-align:center}
.card-image{height:170px;background:var(--card);position:relative;display:flex;align-items:center;justify-content:center}
.card-photo{width:130px;height:110px;border-radius:50%;background:radial-gradient(circle,#e9d9a8 0%,#d4b66a 45%,#efefef 75%)}
.card-photo.silver{background:radial-gradient(circle,#f6f6f6 0%,#c9c9c9 45%,#efefef 75%)}
.card-photo.gem{background:radial-gradient(circle,#e8c3b8 0%,#c9a24a 40%,#efefef 75%)}
.card-photo.aqua{background:radial-gradient(circle,#d8eef0 0%,#9fc9cf 45%,#efefef 75%)}
.heart{position:absolute;right:10px;top:10px}
.quick-view{position:absolute;left:50%;top:50%;transform:translate(-50%,-50%);background:var(--ink);color:var(--white);font-size:10px;font-weight:700;letter-spacing:1px;padding:7px 16px}
.card h4{font-size:12px;font-weight:700;color:var(--ink);margin-top:12px;letter-spacing:.5px}
.price{font-size:16px;font-weight:700;color:var(--gold);margin-top:2px}
.price s{font-size:11px;color:var(--muted);font-weight:400;margin-left:4px}
.card p{font-size:10px;color:var(--muted);line-height:1.4;margin:4px 24px 0}

.more{display:block;width:150px;margin:44px auto 0;background:var(--gold);color:var(--white);text-align:center;font-size:11px;font-weight:700;letter-spacing:1px;padding:11px 0}

/* footer */
.site-footer{position:absolute;left:0;top:2020px;width:1200px;height:328px;background:var(--footer);color:#bdbdbd}
.footer-cols{display:flex;justify-content:space-between;padding-top:48px}
.footer-col h5{font-size:11px;font-weight:700;color:var(--white);letter-spacing:.5px;margin-bottom:14px}
.footer-col a{display:block;font-size:10px;color:#bdbdbd;text-decoration:none;line-height:20px}
.socials{display:flex;gap:8px}
.socials span{width:24px;height:24px;border-radius:50%;background:#4a4a4a}
.newsletter input{display:block;width:200px;height:30px;border:none;background:var(--white);font-family:inherit;font-size:10px;padding:0 10px;color:var(--muted)}
.newsletter .submit{display:inline-block;margin-top:10px;background:var(--gold);color:var(--white);font-size:10px;font-weight:700;letter-spacing:1px;padding:7px 16px}
.copyright{position:absolute;left:0;bottom:0;width:100%;height:44px;background:var(--footer-bottom);font-size:10px;text-align:center;line-height:44px;color:#999}
</style>
</head>
<body>

<header class="site-header">
  <div class="wrap" style="height:128px">
    <div class="utility-bar">
      <span>ABOUT US</span><span>WISHLIST</span><span>SIGN IN</span><span class="bag">0 ITEMS</span>
    </div>
    <div class="brand">
      <div class="brand-mark"></div>
      <div>
        <div class="brand-name">VELISSE</div>
        <div class="brand-tag">Jewellery you'll fall in love with</div>
      </div>
    </div>
    <nav class="main-nav">
      <a class="active" href="#">HOME</a><a href="#">PRODUCTS</a><a href="#">OUR STORY</a><a href="#">CONTACT US</a><a href="#">FAQ</a><a href="#">MY ACCOUNT</a>
    </nav>
  </div>
</header>

<section class="hero" role="img" aria-label="Portrait of a woman wearing drop earrings on a dark background">
  <div class="hero-copy">We celebrate<strong>women here!</strong></div>
  <div class="hero-dots"><span class="on"></span><span></span><span></span><span></span><span></span></div>
</section>

<main class="wrap">
  <section class="offers">
    <div class="offer" role="img" aria-label="Gold jewellery promotion">
      <div class="offer-title">GOLD</div>
      <div class="offer-line">Extra <b>10% off</b></div>
      <div class="offer-sub">for orders over</div>
      <div class="offer-amount">$500</div>
      <div class="offer-date">Till March 31st, 2018</div>
    </div>
    <div class="offer" role="img" aria-label="Diamond rings promotion">
      <div class="offer-title">DIAMOND</div>
      <div class="offer-line">Extra <b>10% off</b></div>
      <div class="offer-sub">DIAMOND RINGS</div>
      <div class="offer-amount">&nbsp;</div>
      <div class="offer-date">Till March 31st, 2018</div>
    </div>
    <div class="offer" role="img" aria-label="Silver jewellery promotion">
      <div class="offer-title">SILVER</div>
      <div class="offer-line">Extra <b>15% off</b></div>
      <div class="offer-sub">for orders over</div>
      <div class="offer-amount">$200</div>
      <div class="offer-date">Till March 31st, 2018</div>
    </div>
  </section>

  <section class="shop">
    <aside class="filters">
      <h2>FILTER BY</h2>
      <div class="filter-group"><h3>TYPE</h3>
        <ul><li>Rings</li><li>Necklaces</li><li>Bracelets</li><li>Earrings</li><li>Charms</li></ul>
      </div>
      <div class="filter-group"><h3>COLLECTION</h3>
        <ul><li>Gold</li><li>Silver</li><li>Diamond</li><li>Pearl</li><li>Sapphire</li><li>Emerald</li><li>Amethyst</li></ul>
      </div>
      <div class="filter-group"><h3>METAL</h3>
        <ul><li>9K Yellow Gold</li><li>14K Rose Gold</li><li>14K White Gold</li><li>18K Yellow Gold</li><li>18K White Gold</li><li>Platinum</li><li>Sterling Silver</li></ul>
      </div>
      <div class="filter-group"><h3>GEMSTONE</h3>
        <ul><li>Amethyst</li><li>Aquamarine</li><li>Sapphire</li><li>Topaz</li><li>Peridot</li><li>Citrine</li><li>Cubic Zirconia</li><li>Emerald</li><li>Garnet</li><li>Diamond</li><li>Opal</li><li>Ruby</li><li>Tanzanite</li></ul>
      </div>
      <div class="filter-group"><h3>PRICE RANGE</h3>
        <div class="price-range"><div class="track"></div><div class="knob" style="left:0"></div><div class="knob" style="right:0"></div></div>
        <div class="price-values"><span>$0</span><span>$1000</span></div>
      </div>
    </aside>

    <div class="products">
      <div class="products-head">
        <h2>OUR PRODUCTS</h2>
        <div class="sorters"><span>Best Sellers ▾</span><span>Show 9 items ▾</span><span>Price ▾</span></div>
      </div>
      <div class="grid">
        <div class="card"><div class="card-image"><div class="card-photo" role="img" aria-label="Pair of gold rings"></div><svg class="heart" width="14" height="13" viewBox="0 0 14 13"><path d="M7 12 1.5 6.5A3 3 0 0 1 7 2.5a3 3 0 0 1 5.5 4Z" fill="none" stroke="#999" stroke-width="1.2"/></svg></div><h4>RING</h4><div class="price">$29.99<s>$49.99</s></div><p>Handpicked piece crafted to be worn and loved every day.</p></div>
        <div class="card"><div class="card-image"><div class="card-photo" role="img" aria-label="Gold ring with stones"></div><span class="quick-view">QUICK VIEW</span><svg class="heart" width="14" height="13" viewBox="0 0 14 13"><path d="M7 12 1.5 6.5A3 3 0 0 1 7 2.5a3 3 0 0 1 5.5 4Z" fill="none" stroke="#999" stroke-width="1.2"/></svg></div><h4>RING</h4><div class="price">$29.99<s>$49.99</s></div><p>Handpicked piece crafted to be worn and loved every day.</p></div>
        <div class="card"><div class="card-image"><div class="card-photo" role="img" aria-label="Gold bracelet"></div><svg class="heart" width="14" height="13" viewBox="0 0 14 13"><path d="M7 12 1.5 6.5A3 3 0 0 1 7 2.5a3 3 0 0 1 5.5 4Z" fill="none" stroke="#999" stroke-width="1.2"/></svg></div><h4>BRACELET</h4><div class="price">$49.99<s>$69.99</s></div><p>Handpicked piece crafted to be worn and loved every day.</p></div>
        <div class="card"><div class="card-image"><div class="card-photo" role="img" aria-label="Wide gold bracelet"></div><svg class="heart" width="14" height="13" viewBox="0 0 14 13"><path d="M7 12 1.5 6.5A3 3 0 0 1 7 2.5a3 3 0 0 1 5.5 4Z" fill="none" stroke="#999" stroke-width="1.2"/></svg></div><h4>BRACELET 1</h4><div class="price">$99.99<s>$129.99</s></div><p>Handpicked piece crafted to be worn and loved every day.</p></div>
        <div class="card"><div class="card-image"><div class="card-photo" role="img" aria-label="Gold drop earrings"></div><svg class="heart" width="14" height="13" viewBox="0 0 14 13"><path d="M7 12 1.5 6.5A3 3 0 0 1 7 2.5a3 3 0 0 1 5.5 4Z" fill="none" stroke="#999" stroke-width="1.2"/></svg></div><h4>EARRINGS</h4><div class="price">$69.99<s>$89.99</s></div><p>Handpicked piece crafted to be worn and loved every day.</p></div>
        <div class="card"><div class="card-image"><div class="card-photo gem" role="img" aria-label="Necklace with red stones"></div><svg class="heart" width="14" height="13" viewBox="0 0 14 13"><path d="M7 12 1.5 6.5A3 3 0 0 1 7 2.5a3 3 0 0 1 5.5 4Z" fill="none" stroke="#999" stroke-width="1.2"/></svg></div><h4>NECKLACES 1</h4><div class="price">$59.99<s>$79.99</s></div><p>Handpicked piece crafted to be worn and loved every day.</p></div>
        <div class="card"><div class="card-image"><div class="card-photo silver" role="img" aria-label="Silver necklace"></div><svg class="heart" width="14" height="13" viewBox="0 0 14 13"><path d="M7 12 1.5 6.5A3 3 0 0 1 7 2.5a3 3 0 0 1 5.5 4Z" fill="none" stroke="#999" stroke-width="1.2"/></svg></div><h4>NECKLACES 2</h4><div class="price">$39.99<s>$59.99</s></div><p>Handpicked piece crafted to be worn and loved every day.</p></div>
        <div class="card"><div class="card-image"><div class="card-photo aqua" role="img" aria-label="Silver necklace with blue stones"></div><svg class="heart" width="14" height="13" viewBox="0 0 14 13"><path d="M7 12 1.5 6.5A3 3 0 0 1 7 2.5a3 3 0 0 1 5.5 4Z" fill="none" stroke="#999" stroke-width="1.2"/></svg></div><h4>NECKLACES 3</h4><div class="price">$69.99<s>$89.99</s></div><p>Handpicked piece crafted to be worn and loved every day.</p></div>
        <div class="card"><div class="card-image"><div class="card-photo" role="img" aria-label="Gold pendant necklace"></div><svg class="heart" width="14" height="13" viewBox="0 0 14 13"><path d="M7 12 1.5 6.5A3 3 0 0 1 7 2.5a3 3 0 0 1 5.5 4Z" fill="none" stroke="#999" stroke-width="1.2"/></svg></div><h4>NECKLACES 4</h4><div class="price">$39.99<s>$59.99</s></div><p>Handpicked piece crafted to be worn and loved every day.</p></div>
      </div>
      <span class="more">VIEW MORE ITEMS</span>
    </div>
  </section>
</main>

<footer class="site-footer">
  <div class="wrap footer-cols">
    <div class="footer-col"><h5>ABOUT US</h5><a href="#">Our Story</a><a href="#">Wholesale Inquiries</a></div>
    <div class="footer-col"><h5>SHOPPING</h5><a href="#">Orders</a><a href="#">Wishlist</a><a href="#">Size Guide</a></div>
    <div class="footer-col"><h5>CUSTOMER CARE</h5><a href="#">Returns</a><a href="#">FAQ</a><a href="#">Gifts &amp; Warranty</a><a href="#">Contact Us</a></div>
    <div class="footer-col"><h5>FOLLOW US</h5><div class="socials"><span></span><span></span><span></span></div></div>
    <div class="footer-col newsletter"><h5>NEWSLETTER</h5><input type="text" value="E-mail"><span class="submit">SUBMIT</span></div>
  </div>
  <div class="copyright">Copyright © 2017 All Rights Reserved</div>
</footer>

</body>
</html>
```